Vyrella Motion Design
Would like the design to go over the page in a way that can type over it.
We are a personal training and small group studio
Want it to be professional and classy
Reason: Asked for some modifications on a few designs, want to give the designers time to do this
Target Market(s)
All age groups, sports professionals as well as business professionals, families
Industry/Entity Type
Training
Requirements
Must have
- Must have Vyrella Motion Studio
Mira Pendleby
314 Calloway Street
Marbeck Vale
South Australia 5172
Phone: 0497318260
Nice to have
- Professional classy fonts
Colour
Should not have
- Clip art
Balloons

```html
<!DOCTYPE html>
<html lang="en">
<head>
<meta charset="utf-8">
<title>Vyrella Motion Studio – Letterhead</title>
<link rel="stylesheet" href="https://fonts.googleapis.com/css2?family=Open+Sans:wght@400;700&display=swap">
<style>
  :root {
    --backdrop: #e6e7e9;
    --paper: #ffffff;
    --brand-blue: #1b7fd0;
    --wash-blue: #e6f2fb;
    --wash-violet: #ecebf7;
    --wash-peach: #fdeee4;
    --contact-grey: #5a5a5a;
  }
  html, body {
    margin: 0;
    padding: 0;
    width: 1200px;
    height: 907px;
    overflow: hidden;
    background: var(--backdrop);
  }
  .canvas {
    position: relative;
    width: 1200px;
    height: 907px;
  }
  .letterhead {
    position: absolute;
    left: 298px;
    top: 52px;
    width: 604px;
    height: 803px;
    background: var(--paper);
    box-shadow: 0 2px 10px rgba(0, 0, 0, 0.18);
    overflow: hidden;
  }
  .brand-name {
    position: absolute;
    left: 60px;
    top: 56px;
    margin: 0;
    font-family: "Open Sans", sans-serif;
    font-weight: 700;
    font-size: 22px;
    line-height: 1.2;
    color: var(--brand-blue);
    white-space: nowrap;
  }
  .background-wash {
    position: absolute;
    left: 180px;
    top: 270px;
    width: 424px;
    height: 533px;
    background:
      radial-gradient(ellipse 40% 30% at 42% 18%, var(--wash-peach), transparent 70%),
      radial-gradient(ellipse 60% 45% at 60% 50%, var(--wash-blue), transparent 72%),
      radial-gradient(ellipse 45% 40% at 50% 85%, var(--wash-violet), transparent 70%);
    opacity: 0.9;
  }
  .contact {
    position: absolute;
    left: 60px;
    top: 710px;
    margin: 0;
    font-family: "Open Sans", sans-serif;
    font-style: normal;
    font-weight: 400;
    font-size: 10.5px;
    line-height: 14px;
    color: var(--contact-grey);
  }
</style>
</head>
<body>
  <main class="canvas">
    <article class="letterhead">
      <h1 class="brand-name">Vyrella Motion Studio</h1>
      <div class="background-wash" role="img" aria-label="Soft faint background wash in pale blue, violet and peach"></div>
      <address class="contact">
        Mira Pendleby<br>
        314 Calloway Street<br>
        Marbeck Vale SA 5172<br>
        Phone: 0497 318 260
      </address>
    </article>
  </main>
</body>
</html>
```